Plomberie TRV est une nouvelle entreprise de plomberie

Jaimerais maintenant des carte daffaire

Tendance
Avec un petit Puntch

Jaimerais quelque chose dans ce style avec le logo foncé plomberie trv en facade
Jaimerais une photo en backgroung de fitting de plomberie comme je vous ai envoyer

Si vous voulez chercher une photo marquer sur google ( fitting kolbar) pour vous donner des idee
Je veux que les fitting soit dune couleur pale en back ground pour faire ressortir mon logo

Toujours en facade de la carte je veux quil y ai mes services d'inscrit

Construction neuve
Reparation
Renovation
Urgence

438-206-5917
Julien fortier

A larriere de la carte jaimerais le logo pâle plomberie TRV
Avec mes info
Email: info.trvconstruction@exemplemail.com
Julien fortier
Cell: 438-206-5917
Plomberietrv.com

Voici des design que jai bien aimer libre a vous de vous laisser aller plus loin

Merci au plaisir de travailler avec vous

30 a 60 ans contracteur general

Construction plomberie

Plomberie TRV inc. 438-206-5917 Julien fortier. Plombier. info.trvconstruction@exemplemail.com

Sans Serif

0054AA
0677BA
7BADD7
CADEEF
E8F1F8
F0912C
F2A743
F7CA91
FBE8D2
FDF5EE
EE7325
F08F49
F5BC92
FAE3D3
FDF4ED

• Plombier serieux et virile jaime la couleur cuivre comme les fitting
• Carte transparente

```html
<!DOCTYPE html>
<html lang="fr">
<head>
<meta charset="utf-8">
<title>Plomberie TRV – cartes d'affaires</title>
<link href="https://fonts.googleapis.com/css2?family=Montserrat:wght@500;600;700;800&display=swap" rel="stylesheet">
<style>
  :root {
    --page: #e4e2e0;
    --card-dark: #1d1b1a;
    --card-dark-2: #272422;
    --stripe-grey: #34312f;
    --copper-light: #c47a3d;
    --copper: #a9592a;
    --copper-deep: #843c1b;
    --white: #ffffff;
    --frame-grey: #3b3836;
  }
  * { box-sizing: border-box; margin: 0; padding: 0; }
  html, body {
    width: 1200px; height: 780px; overflow: hidden;
    background: var(--page);
    font-family: "Montserrat", sans-serif;
  }
  .canvas { position: relative; width: 1200px; height: 780px; }

  .card {
    position: absolute;
    width: 540px; height: 309px;
    border-radius: 20px;
    overflow: hidden;
    background: linear-gradient(160deg, var(--card-dark-2), var(--card-dark));
    box-shadow: 0 10px 30px rgba(0,0,0,.25);
    color: var(--white);
  }
  .card--front { left: 50px; top: 70px; }
  .card--back  { left: 610px; top: 400px; }

  .brand-name {
    position: absolute;
    font-weight: 800;
    color: var(--white);
    letter-spacing: 2px;
    text-transform: uppercase;
    display: flex; align-items: center; gap: 10px;
    z-index: 2;
  }
  .brand-mark {
    width: 14px; height: 14px; border-radius: 50%;
    background: var(--white);
  }

  /* front */
  .front-stripe {
    position: absolute; left: 0; right: 0; top: 112px; height: 14px;
    background: var(--stripe-grey);
  }
  .front-band {
    position: absolute; left: 0; right: 0; top: 126px; height: 150px;
    background: linear-gradient(100deg, var(--copper-deep), var(--copper-light) 55%, var(--copper-deep));
  }
  .card--front .brand-name { top: 46px; left: 0; right: 0; justify-content: center; font-size: 32px; }
  .pipe-lines { position: absolute; inset: 0; }
  .services {
    position: absolute; top: 148px; left: 0; right: 0;
    text-align: center; font-weight: 600; font-size: 19px; line-height: 1.25;
  }
  .front-phone {
    position: absolute; top: 200px; left: 0; right: 0;
    text-align: center; font-weight: 700; font-size: 31px; letter-spacing: 1px;
  }
  .front-name {
    position: absolute; top: 241px; left: 0; right: 0;
    text-align: center; font-weight: 500; font-size: 15px;
  }

  /* back */
  .back-frame { position: absolute; inset: 0; }
  .card--back .brand-name { top: 48px; left: 40px; font-size: 28px; }
  .holder-name {
    position: absolute; top: 130px; left: 44px;
    color: var(--copper); font-weight: 800; font-size: 27px; letter-spacing: 1px;
  }
  .holder-mark {
    position: absolute; top: 134px; left: 14px; width: 18px; height: 26px;
    border: 6px solid var(--copper); border-left: none;
  }
  .contact-list { position: absolute; top: 175px; left: 44px; list-style: none; }
  .contact-item {
    display: flex; align-items: center; gap: 12px;
    font-weight: 600; font-size: 17px; height: 36px;
  }
  .contact-icon {
    width: 24px; height: 24px; border-radius: 50%; background: var(--white);
    display: flex; align-items: center; justify-content: center; flex: none;
  }
</style>
</head>
<body>
<main class="canvas">

  <section class="card card--front" aria-label="Recto de la carte">
    <div class="front-stripe"></div>
    <div class="front-band"></div>
    <div class="brand-name"><span class="brand-mark"></span>Plomberie TRV</div>
    <svg class="pipe-lines" width="540" height="309" viewBox="0 0 540 309">
      <g stroke="#ffffff" stroke-width="3" fill="none">
        <line x1="30" y1="262" x2="190" y2="262"/>
        <line x1="190" y1="254" x2="190" y2="270"/>
        <line x1="405" y1="220" x2="520" y2="220"/>
        <line x1="405" y1="212" x2="405" y2="228"/>
      </g>
    </svg>
    <p class="services">Construction neuve • Reparation<br>Renovation • Urgence</p>
    <p class="front-phone">438-206-5917</p>
    <p class="front-name">Julien fortier</p>
  </section>

  <section class="card card--back" aria-label="Verso de la carte">
    <svg class="back-frame" width="540" height="309" viewBox="0 0 540 309">
      <polyline points="365,80 470,80 500,125 500,170 540,170" stroke="#3b3836" stroke-width="10" fill="none"/>
    </svg>
    <div class="brand-name"><span class="brand-mark"></span>Plomberie TRV</div>
    <span class="holder-mark"></span>
    <p class="holder-name">JULIEN FORTIER</p>
    <ul class="contact-list">
      <li class="contact-item">
        <span class="contact-icon">
          <svg width="14" height="14" viewBox="0 0 24 24"><path fill="#1d1b1a" d="M6.6 10.8a15 15 0 0 0 6.6 6.6l2.2-2.2a1 1 0 0 1 1-.25 11.4 11.4 0 0 0 3.6.57 1 1 0 0 1 1 1V20a1 1 0 0 1-1 1A17 17 0 0 1 3 4a1 1 0 0 1 1-1h3.5a1 1 0 0 1 1 1c0 1.25.2 2.45.57 3.57a1 1 0 0 1-.25 1z"/></svg>
        </span>438-206-5917
      </li>
      <li class="contact-item">
        <span class="contact-icon">
          <svg width="14" height="14" viewBox="0 0 24 24"><rect x="3" y="6" width="18" height="12" rx="1" fill="none" stroke="#1d1b1a" stroke-width="2"/><polyline points="3,7 12,13 21,7" fill="none" stroke="#1d1b1a" stroke-width="2"/></svg>
        </span>info.trvconstruction@exemplemail.com
      </li>
      <li class="contact-item">
        <span class="contact-icon">
          <svg width="14" height="14" viewBox="0 0 24 24"><g fill="none" stroke="#1d1b1a" stroke-width="2"><circle cx="12" cy="12" r="9"/><ellipse cx="12" cy="12" rx="4" ry="9"/><line x1="3" y1="12" x2="21" y2="12"/></g></svg>
        </span>plomberietrv.com
      </li>
    </ul>
  </section>

</main>
</body>
</html>
```